Fabric Store Business card

Need a business card portraying store logo and up and coming business of quilt fabrics, apparel fabrics, notions and buttons. Our business name is Gilded Thimble and Such. Am attaching logo. The design should communicate a growing business and warm atmosphere. Would like address and store hours and contact info displayed on card. Mon - Fri 9:30 to 5:00, Saturday 9:30 to 1:00. Address 287 W Alder Ave, Newton, KS 67392 email: gildedthimbleandsuch@mailbrook.net. Phone and fax 316-555-2846. After hours contact # 620-555-3914 Also like vintage sewing machines and dress forms if it works to incorporate fine, if not thats ok too.

```html
<!DOCTYPE html>
<html lang="en">
<head>
<meta charset="utf-8">
<title>Gilded Thimble and Such – Business Card</title>
<link href="https://fonts.googleapis.com/css2?family=Open+Sans:wght@400;600&display=swap" rel="stylesheet">
<style>
  :root {
    --backdrop: #e4e4e4;
    --crimson: #8e1b26;
    --crimson-deep: #7a141f;
    --crimson-soft: #9c2531;
    --paper: #ffffff;
    --ink: #2b2b2b;
    --blush: #f1dcdc;
  }
  * { box-sizing: border-box; margin: 0; padding: 0; }
  html, body { width: 1200px; height: 900px; overflow: hidden; }
  body {
    background: var(--backdrop);
    font-family: "Open Sans", Arial, sans-serif;
    position: relative;
  }
  .card {
    position: absolute;
    top: 290px;
    width: 530px;
    height: 320px;
    border-radius: 26px;
    overflow: hidden;
    box-shadow: 0 10px 24px rgba(0,0,0,0.18);
  }
  .card--front { left: 50px; background: var(--paper); }
  .card--back { left: 620px; background: var(--crimson); }

  .card__frame {
    position: absolute;
    inset: 12px;
    border-radius: 18px;
    pointer-events: none;
  }
  .card--front .card__frame { border: 9px solid var(--crimson); }
  .card--back .card__frame { border: 4px solid var(--paper); inset: 14px; }
  .card--back::before {
    content: "";
    position: absolute;
    inset: 0;
    border-radius: 26px;
    border: 10px solid var(--crimson-deep);
  }

  .brand {
    position: absolute;
    display: flex;
    align-items: center;
    gap: 14px;
  }
  .brand__dot { border-radius: 50%; flex: none; }
  .brand__name {
    font-family: "Open Sans", Arial, sans-serif;
    font-weight: 400;
    font-size: 30px;
    line-height: 1.1;
  }
  .card--front .brand { left: 78px; top: 68px; }
  .card--front .brand__dot { width: 52px; height: 52px; background: var(--crimson); }
  .card--front .brand__name { color: var(--crimson); }
  .card--back .brand { left: 110px; top: 127px; }
  .card--back .brand__dot { width: 60px; height: 60px; background: var(--paper); }
  .card--back .brand__name { color: var(--paper); }

  .faint-disc {
    position: absolute;
    left: 10px; top: 186px;
    width: 140px; height: 140px;
    border-radius: 50%;
    background: var(--blush);
    opacity: 0.7;
  }

  .details {
    position: absolute;
    left: 30px; top: 188px;
    display: flex;
    gap: 12px;
    font-size: 13.5px;
    color: var(--ink);
  }
  .details__hours { text-align: right; line-height: 1.45; width: 148px; }
  .details__owners { color: var(--crimson); font-weight: 600; margin-top: 4px; }
  .details__role { color: var(--crimson); font-size: 11px; }
  .details__rule { width: 1.5px; background: var(--crimson); }
  .details__contact { line-height: 1.55; }
  .details__label { color: var(--crimson); }

  .motif {
    position: absolute;
    background: var(--crimson-soft);
    opacity: 0.55;
  }
  .motif--form { left: 22px; top: 30px; width: 92px; height: 260px; border-radius: 40px 40px 8px 8px; }
  .motif--machine { right: 28px; top: 145px; width: 130px; height: 145px; border-radius: 30px 10px 8px 8px; }
</style>
</head>
<body>
  <section class="card card--front" aria-label="Business card front">
    <div class="faint-disc"></div>
    <div class="card__frame"></div>
    <div class="brand">
      <span class="brand__dot"></span>
      <span class="brand__name">Gilded Thimble<br>and Such</span>
    </div>
    <div class="details">
      <div class="details__hours">
        <div>Mon - Fri 9:30 to 5:00</div>
        <div>Saturday 9:30 to 1:00</div>
        <div class="details__owners">Dale &amp; Marnie Voskuil</div>
        <div class="details__role">Owners</div>
      </div>
      <div class="details__rule"></div>
      <div class="details__contact">
        <div>287 W Alder Ave, Newton, KS 67392</div>
        <div><span class="details__label">email:</span> gildedthimbleandsuch@mailbrook.net</div>
        <div><span class="details__label">Phone and fax:</span> 316-555-2846.</div>
        <div><span class="details__label">After hours contact :</span> 620-555-3914</div>
      </div>
    </div>
  </section>

  <section class="card card--back" aria-label="Business card back">
    <div class="motif motif--form" role="img" aria-label="Faint illustration of a vintage dress form"></div>
    <div class="motif motif--machine" role="img" aria-label="Faint illustration of a vintage sewing machine"></div>
    <div class="card__frame"></div>
    <div class="brand">
      <span class="brand__dot"></span>
      <span class="brand__name">Gilded Thimble<br>and Such</span>
    </div>
  </section>
</body>
</html>
```